Smile club flyer design

I am launching an office smile club and would like a design that sits my branding and that is appealing to customers. I have a design (I need a new one) that has all the information.
My website is maplecrestdentalcarewv.com
Brand color is green. The design can be any color

Target Market(s)

Ages 30+

Industry/Entity Type

Dental

Font styles to use
Serif

Requirements
Must have
• Appealing to patients

```html
<!DOCTYPE html>
<html lang="en">
<head>
<meta charset="utf-8">
<title>Maplecrest Dental Care – Smile Club Membership</title>
<link href="https://fonts.googleapis.com/css2?family=Allura&family=Bebas+Neue&family=Jost:wght@400;500;700&family=Libre+Baskerville:wght@400;700&display=swap" rel="stylesheet">
<style>
  :root{
    --teal:#00827a;
    --mint:#b8e2da;
    --slate:#6c6d70;
    --ink:#4a4a4c;
    --stage:#444446;
    --paper:#ffffff;
    --wash:#f1f1f1;
  }
  *{box-sizing:border-box;margin:0;padding:0}
  html,body{width:904px;height:1200px;overflow:hidden;background:var(--stage)}
  .flyer{
    position:absolute;left:27px;top:0;width:1300px;height:1838px;
    background:var(--paper);transform:scale(.6529);transform-origin:0 0;
    font-family:"Jost",sans-serif;color:var(--ink);overflow:hidden;
  }
  .pattern-wash{position:absolute;left:0;right:0;top:120px;bottom:0;
    background:radial-gradient(ellipse at 50% 45%,var(--paper) 35%,var(--wash) 100%)}
  .header-band{position:absolute;left:0;top:0;width:1300px;height:170px}
  .brand{position:absolute;left:0;right:0;top:28px;text-align:center;color:var(--paper)}
  .brand-name{font-family:"Libre Baskerville",serif;font-size:60px;line-height:1;letter-spacing:-1px}
  .brand-sub{font-family:"Libre Baskerville",serif;font-size:25px;letter-spacing:8px;margin-top:10px}

  .title-panel{position:absolute;left:413px;top:150px;width:474px;height:435px;background:var(--mint);border-radius:0 0 22px 22px}
  .intro{position:absolute;left:300px;top:150px;width:720px;text-align:center;font-family:"Allura",cursive;font-size:170px;color:var(--ink);line-height:1;white-space:nowrap}
  .club{position:absolute;left:0;right:0;top:290px;text-align:center;font-family:"Bebas Neue",sans-serif;font-size:222px;line-height:1;color:var(--teal);white-space:nowrap;transform:scaleX(.9)}
  .membership{position:absolute;left:0;right:0;top:484px;text-align:center;font-family:"Bebas Neue",sans-serif;font-size:90px;line-height:1;color:var(--ink);letter-spacing:8px;white-space:nowrap}
  .tagline{position:absolute;left:0;right:0;top:602px;text-align:center;font-size:40px;color:var(--ink);white-space:nowrap}
  .tagline strong{font-weight:700}

  .tier{position:absolute;left:106px;width:1088px;height:226px}
  .tier-panel{position:absolute;left:200px;top:0;right:0;bottom:0;border-radius:0 24px 24px 0;padding:10px 0 0 80px}
  .price-box{position:absolute;left:0;top:0;width:232px;height:226px;background:var(--paper);border:7px solid;border-radius:20px;box-shadow:6px 0 6px rgba(0,0,0,.25)}
  .price{position:absolute;left:18px;top:6px;font-family:"Bebas Neue",sans-serif;line-height:1}
  .price .cur{font-size:90px;vertical-align:top;position:relative;top:58px}
  .price .num{font-size:190px}
  .per{position:absolute;left:0;right:0;bottom:10px;text-align:center;font-size:40px}
  .tier h2{font-size:37px;font-weight:400;letter-spacing:.5px;margin-bottom:4px;white-space:nowrap}
  .tier h2 b{font-weight:700}
  .tier ul{list-style:none}
  .tier li{font-size:32px;line-height:37.5px;position:relative;padding-left:52px;margin-left:-20px;white-space:nowrap}
  .tier li::before{content:"";position:absolute;left:0;top:14px;width:18px;height:12px;border-radius:50% 50% 40% 40%;background:currentColor;opacity:.9}
  .tier-rate{position:absolute;right:34px;bottom:12px;font-size:30px;white-space:nowrap}
  .tier--core .price-box{border-color:var(--teal);color:var(--teal)}
  .tier--core .tier-panel{background:var(--teal);color:var(--paper)}
  .tier--cosmetic .price-box{border-color:var(--slate);color:var(--slate)}
  .tier--cosmetic .tier-panel{background:var(--slate);color:var(--mint)}
  .tier--cosmetic h2{color:var(--mint)}
  .tier--cosmetic ul{margin-top:18px}
  .tier--perio .price-box{border-color:var(--teal);color:var(--teal)}
  .tier--perio .tier-panel{background:var(--mint);color:var(--teal)}
  .tier--perio .tier-rate{right:14px;bottom:2px}

  .join-head{position:absolute;left:69px;top:1468px;font-size:37px;color:var(--ink);white-space:nowrap}
  .phone{position:absolute;left:69px;top:1512px;font-family:"Bebas Neue",sans-serif;font-size:104px;line-height:1;color:var(--teal);white-space:nowrap;transform:scaleX(.91);transform-origin:0 0}
  .finance{position:absolute;left:69px;top:1620px;font-size:26px;letter-spacing:.3px;white-space:nowrap}
  .plans{position:absolute;left:69px;top:1680px;font-size:24px;line-height:30px;white-space:nowrap}
  .partner{position:absolute;left:296px;font-weight:700;font-size:34px;line-height:44px;white-space:nowrap;display:flex;align-items:center;gap:10px}
  .partner i{display:inline-block;width:26px;height:26px;border-radius:50%}
  .partner--one{top:1652px;color:var(--teal)}
  .partner--one i{background:var(--teal)}
  .partner--two{top:1710px;color:#222}
  .partner--two i{background:#e2574c}
  .fee{position:absolute;left:69px;top:1758px;font-size:20px;white-space:nowrap}

  .offer-tab{position:absolute;left:632px;top:1478px;width:270px;height:256px;background:var(--ink);border-radius:24px}
  .offer-tab span{position:absolute;left:64px;top:8px;font-family:"Libre Baskerville",serif;font-size:26px;letter-spacing:8px;color:var(--paper);font-weight:700}
  .offer{position:absolute;left:664px;top:1525px;width:556px;height:236px;background:var(--mint);border-radius:24px;box-shadow:4px 6px 8px rgba(0,0,0,.2);color:var(--teal)}
  .offer h3{position:absolute;left:29px;top:10px;font-size:36px;font-weight:400;white-space:nowrap}
  .offer h3 b{font-weight:700}
  .offer-price{position:absolute;left:24px;top:36px;font-family:"Bebas Neue",sans-serif;color:var(--ink);line-height:1;white-space:nowrap;transform:scaleX(.9);transform-origin:0 0}
  .offer-price .cur{font-size:78px;vertical-align:top;position:relative;top:58px}
  .offer-price .num{font-size:176px}
  .offer-list{position:absolute;left:267px;top:62px;font-size:28px;line-height:46px;white-space:nowrap}
  .offer-note{position:absolute;left:0;right:0;bottom:6px;text-align:center;font-family:"Libre Baskerville",serif;font-size:22px;letter-spacing:10px;color:var(--ink);font-variant:small-caps;white-space:nowrap}
</style>
</head>
<body>
<main class="flyer">
  <div class="pattern-wash" role="img" aria-label="Faint light grey leaf pattern across the background"></div>

  <svg class="header-band" viewBox="0 0 1300 170" aria-hidden="true">
    <path d="M0 0H1300V85Q650 200 0 85Z" fill="#00827a"/>
    <path d="M0 92Q650 208 1300 92" fill="none" stroke="#e6e6e6" stroke-width="6"/>
  </svg>
  <div class="brand">
    <div class="brand-name">Maplecrest</div>
    <div class="brand-sub">— DENTAL CARE —</div>
  </div>

  <div class="title-panel"></div>
  <div class="intro">Introducing</div>
  <div class="club">SMILE CLUB</div>
  <div class="membership">MEMBERSHIP</div>

  <p class="tagline">AFFORDABLE DENTAL CARE | <strong>NO INSURANCE REQUIRED</strong></p>

  <section class="tier tier--core" style="top:687px">
    <div class="tier-panel">
      <h2>CORE CARE <b>PREVENTIVE</b></h2>
      <ul>
        <li>Comprehensive Annual Exam</li>
        <li>2 Professional Cleanings per Year</li>
        <li>Routine Bitewing X-rays</li>
        <li>10% Savings on Treatment</li>
      </ul>
      <span class="tier-rate">$39/MONTH</span>
    </div>
    <div class="price-box"><div class="price"><span class="cur">$</span><span class="num">39</span></div><div class="per">/MONTH</div></div>
  </section>

  <section class="tier tier--cosmetic" style="top:943px">
    <div class="tier-panel">
      <h2>BRIGHT <b>COSMETIC</b></h2>
      <ul>
        <li>Annual In-Office Whitening (Top &amp; Bottom)</li>
        <li>Custom Whitening Trays</li>
        <li>15% Savings on Elective Treatment</li>
      </ul>
      <span class="tier-rate">$59/MONTH</span>
    </div>
    <div class="price-box"><div class="price"><span class="cur">$</span><span class="num">59</span></div><div class="per">/MONTH</div></div>
  </section>

  <section class="tier tier--perio" style="top:1197px">
    <div class="tier-panel">
      <h2>CORE CARE <b>PREVENTIVE</b></h2>
      <ul>
        <li>3-4 Perio Maintenance Visits per Year</li>
        <li>1 Comprehensive Exam</li>
        <li>Diagnostic X-rays</li>
        <li>15% Savings on Restorative &amp; Elective Care</li>
      </ul>
      <span class="tier-rate">$89/MONTH</span>
    </div>
    <div class="price-box"><div class="price"><span class="cur">$</span><span class="num">89</span></div><div class="per">/MONTH</div></div>
  </section>

  <section class="join">
    <p class="join-head">JOIN SMILE CLUB TODAY!</p>
    <p class="phone">304-555-0187</p>
    <p class="finance">FLEXIBLE FINANCING FOR TREATMENT:</p>
    <p class="plans">PAYMENT PLANS<br>AVAILABLE</p>
    <p class="partner partner--one"><i></i>HealthPay Plus</p>
    <p class="partner partner--two"><i></i>Orchard Pay</p>
    <p class="fee">$49 Lifetime Activation Fee (Non-Refundable)</p>
  </section>

  <div class="offer-tab"><span>NEW</span></div>
  <section class="offer">
    <h3><b>SMILE REFRESH</b> PACKAGE</h3>
    <div class="offer-price"><span class="cur">$</span><span class="num">499</span></div>
    <p class="offer-list">Cleaning +<br>Comprehensive Exam +<br>Whitening</p>
    <p class="offer-note">Limited Time Offer</p>
  </section>
</main>
</body>
</html>
```